Fence Contractor Website Design

We are working with Yardline Works. They are a local fencing and automatic gate installer and in need of a new website design.
Some sites to use for inspiration:
https://pinevalebarrier.example
https://marwickrails.example
https://www.tellurpostsandboards.example
https://www.grovanpaneling.example
Thank you for taking the time to consider designing a website for us. We are web developers based in Stockton, CA, USA. Most of our projects go through the same process. Understanding this process may help you win a project with us. We custom-code all of our websites in-house. We don’t have any requirements as to what tools you use for your design, but we prefer Figma files. For any design that we label as four-stars, we send it to the client for review. The client picks the final design they want us to use. Once we complete this process, we will continue to show additional clients all the four-star sites and purchase them later. Your designs will have multiple chances to sell. For better chances of success, we ask that you follow these guidelines.
IMAGES:
If you use any images or icons in the design, we ask that you have a link to the asset so we can purchase the image/icon. Most of the designs we submit do not have the customer’s images on them unless they have some great images. Be creative; show us the feeling you are trying to portray with your image choices. Use any royalty-free site you choose. We subscribe to Stockvane and mainly use their images, but we can purchase images outside of Stockvane.
PLEASE NOTE: we will not submit designs to clients with watermarks on the images.
FONTS:
We ask that you identify the fonts used in the design. This can be done in a message if you want. We typically use Google Fonts and Stockvane Fonts.
CONTENT:
We're always open to different content and ideas. We often submit designs with stock images so the client can see our vision. We typically take pictures after the website launch to use their images with our vision. Lorem Ipsum is fine for paragraphs, but we ask that you write the headers in correct English. We want to be able to show the vision and identify the sections of the website.
INSPIRATION:
We typically add a couple of links in the brief of websites we like to help you get started in your design.
REVISIONS:
We do not often ask for revisions of the designs unless we see something in the design that may not appeal to the client. If there are slight changes that we want to make, we do that in the development process.
FEEDBACK:
We rarely give feedback on designs during the design process. We are working on many website projects and do not have the time to provide feedback. We usually respond if your request is well thought out and asks specific questions, but a note asking “feedback, please” usually goes unanswered.
Number of Pages Required
1 page
Look and feel
Each slider illustrates characteristics of the customer's brand and the style your logo design should communicate.

```html
<!DOCTYPE html>
<html lang="en">
<head>
<meta charset="utf-8">
<title>Yardline Works — Fencing &amp; Gates</title>
<link href="https://fonts.googleapis.com/css2?family=Roboto:wght@300;400;500;700;900&family=Bebas+Neue&family=DM+Serif+Display&display=swap" rel="stylesheet">
<style>
:root{
  --red:#ee1c1c;
  --navy:#1b2642;
  --navy-dark:#16203a;
  --ink:#1d1d1f;
  --text:#555a66;
  --light:#eef2fa;
  --line:#c9ccd3;
  --white:#ffffff;
}
*{box-sizing:border-box;margin:0;padding:0}
html,body{width:1200px;height:5017px;overflow:hidden}
body{position:relative;background:var(--white);font-family:'Roboto',sans-serif;color:var(--ink)}
.abs{position:absolute}
.photo{position:absolute;overflow:hidden}

/* hero */
.hero{left:0;top:0;width:1200px;height:598px;background:linear-gradient(180deg,#4a3c5c 0%,#c97a4a 30%,#e9a45a 45%,#6b4a34 62%,#3d4a2a 80%,#5b7a3a 100%)}
.brand{left:97px;top:44px;color:var(--white);font-weight:900;font-size:22px;letter-spacing:1px;display:flex;align-items:center;gap:10px}
.brand .mark{width:18px;height:18px;background:var(--red)}
.nav{right:105px;top:54px;display:flex;gap:18px}
.nav a{color:var(--white);font-size:13px;font-weight:500;text-decoration:none;letter-spacing:.3px}
.hero-title{left:744px;top:208px;font-family:'DM Serif Display',serif;font-size:54px;line-height:55px;color:var(--white);letter-spacing:-1px}
.strip{left:97px;top:505px;width:998px;height:93px;display:flex;background:var(--white)}
.strip .item{width:308px;display:flex;align-items:center;gap:16px;padding-left:22px;font-size:14px;line-height:17px;color:var(--ink);border-right:1px solid #e3e3e3}
.strip .item.active{background:var(--red);color:var(--white);width:290px}
.strip .thumb{width:66px;height:66px;border-radius:50%;background:linear-gradient(135deg,#c48a56,#6a7d95)}
.strip .arrows{flex:1;display:flex;background:#f0f0f0}
.strip .arrows span{flex:1;display:flex;align-items:center;justify-content:center;color:#888;font-size:22px;border-left:1px solid #ddd}

/* about */
.about-ring{left:97px;top:662px;width:490px;height:490px;border-radius:50%;border:8px dotted var(--navy)}
.about-photo{left:122px;top:682px;width:460px;height:460px;border-radius:50%;background:linear-gradient(150deg,#d9c9a8 0%,#e8c62a 35%,#8c5a3c 60%,#b3a08a 100%);box-shadow:0 0 0 6px #fff}
.eyebrow{color:var(--red);font-size:13px;letter-spacing:.5px}
.about-eyebrow{left:655px;top:700px;display:flex;align-items:center;gap:8px}
.about-eyebrow::before{content:"";width:30px;height:1px;background:var(--red)}
.h2{font-weight:700;font-size:34px;color:var(--ink);letter-spacing:-.5px}
.about-title{left:655px;top:725px}
.about-quote{left:655px;top:782px;width:440px;border-left:4px solid var(--red);padding-left:18px;font-size:12.5px;line-height:21px;color:var(--text)}
.mission-title{left:655px;top:880px;font-size:26px;font-weight:500}
.mission-text{left:655px;top:924px;width:440px;font-size:12.5px;line-height:21px;color:var(--text)}
.btn-dark{left:657px;top:1042px;width:172px;height:45px;background:var(--navy);color:var(--white);font-size:13px;font-weight:500;display:flex;align-items:center;justify-content:center;border-radius:3px}
.demo{left:862px;top:1045px;display:flex;align-items:center;gap:12px;font-size:14px;font-weight:500;color:var(--navy)}
.demo .play{width:38px;height:38px;border-radius:50%;background:var(--red);display:flex;align-items:center;justify-content:center}

/* banner */
.banner{left:97px;top:1204px;width:998px;height:491px;border-radius:16px;background:linear-gradient(180deg,#8fb36a 0%,#5b7f3f 20%,#f3f3f3 28%,#dfe5dc 48%,#4f7a30 60%,#3c6425 100%)}
.banner-notch{left:460px;top:1204px;width:280px;height:32px;background:var(--white);clip-path:polygon(0 0,100% 0,88% 100%,12% 100%)}
.banner-title{left:97px;top:1478px;width:998px;text-align:center;color:var(--white);font-family:'Bebas Neue',sans-serif;font-size:44px;line-height:38px;letter-spacing:.5px}
.banner-text{left:97px;top:1566px;width:998px;text-align:center;color:var(--white);font-size:13px}
.btn-white{left:504px;top:1606px;width:166px;height:44px;background:var(--white);color:var(--ink);font-size:13px;font-weight:500;display:flex;align-items:center;justify-content:center;border-radius:3px}

/* services */
.section-title{left:0;width:1200px;text-align:center}
.services-title{top:1743px}
.card{width:238px;height:234px;background:var(--white);box-shadow:0 2px 10px rgba(0,0,0,.1);text-align:center;overflow:hidden}
.card .icon{width:78px;height:78px;background:var(--red);margin:36px auto 16px;display:flex;align-items:center;justify-content:center}
.card h3{font-size:16px;font-weight:500;margin-bottom:8px}
.card p{font-size:11px;line-height:19px;color:var(--text);padding:0 22px}
.card::after{content:"";position:absolute;right:0;bottom:0;width:42px;height:42px;background:var(--navy);clip-path:polygon(100% 0,100% 100%,0 100%)}

/* cta */
.cta{left:0;top:2406px;width:1200px;height:325px;background:repeating-linear-gradient(90deg,#1c2744 0 36px,#19233e 36px 40px)}
.cta h2{position:absolute;top:70px;width:1200px;text-align:center;color:var(--white);font-family:'Bebas Neue',sans-serif;font-size:78px;letter-spacing:-1px}
.cta p{position:absolute;top:152px;width:1200px;text-align:center;color:#dfe3ee;font-size:24px;font-weight:300}
.btn-red{background:var(--red);color:var(--white);font-weight:500;display:flex;align-items:center;justify-content:center;gap:8px}
.cta .btn-red{position:absolute;left:500px;top:208px;width:201px;height:52px;border-radius:26px;font-size:17px}

/* work */
.work-eyebrow{top:2797px;font-size:18px;font-weight:500;color:var(--red)}
.work-title{top:2822px;font-size:44px}
.dots{left:565px;top:3343px;display:flex;gap:6px}
.dots span{width:7px;height:7px;border-radius:50%;background:#ccc}
.dots span:first-child{background:var(--red)}
.work-label{left:355px;top:3222px;width:480px;height:68px;background:rgba(255,255,255,.82);display:flex;align-items:center;padding-left:28px;font-size:15px;font-weight:500;color:var(--ink)}

/* feedback */
.feedback-title{top:3395px;font-size:34px;font-weight:500;line-height:41px}
.review{width:487px;height:187px;background:var(--light);padding:30px 44px}
.review::after{content:"";position:absolute;left:56px;bottom:-18px;border:18px solid transparent;border-top-color:var(--light);border-bottom:0}
.stars{display:flex;gap:10px;margin-bottom:14px}
.stars span{width:20px;height:20px;background:#f7a813;clip-path:polygon(50% 0,61% 35%,98% 35%,68% 57%,79% 91%,50% 70%,21% 91%,32% 57%,2% 35%,39% 35%)}
.review p{font-size:12.5px;line-height:21px;color:var(--text)}
.person{display:flex;align-items:center;gap:16px}
.person .avatar{width:72px;height:72px;border-radius:50%;background:linear-gradient(180deg,#c9d3e2,#4b5a78)}
.person b{display:block;font-size:14px;font-weight:500;color:#444}
.person small{font-size:11px;color:#999}

/* contact */
.contact-bg{left:0;top:3876px;width:1200px;height:575px;background:var(--light)}
.contact-title{left:97px;top:3940px;font-size:38px}
.field{background:var(--white);border:1px solid var(--line);font-size:11px;color:#888;padding:14px 16px}
.btn-submit{left:97px;top:4291px;width:178px;height:51px;font-size:16px;font-weight:700;border-radius:2px}
.contact-photo{left:641px;top:3933px;width:454px;height:450px;background:linear-gradient(180deg,#3a7ac6 0%,#7fb0e4 45%,#e9eef4 50%,#dfe3ea 100%)}

/* footer */
.footer{left:0;top:4451px;width:1200px;height:487px;background:var(--navy-dark)}
.signup-title{top:4510px;color:var(--white);font-size:32px;font-weight:500}
.signup-input{left:257px;top:4597px;width:472px;height:55px;border:1px solid #8a92a8;border-radius:3px;display:flex;align-items:center;gap:12px;padding-left:24px;font-size:12px;color:#c9ceda}
.btn-sub{left:744px;top:4597px;width:193px;height:55px;font-size:15px;border-radius:3px}
.foot-brand{left:97px;top:4785px;color:var(--white);font-weight:900;font-size:28px;letter-spacing:1px;display:flex;align-items:center;gap:12px}
.foot-brand .mark{width:22px;height:22px;background:var(--white)}
.foot-col h4{color:var(--white);font-size:16px;font-weight:700;margin-bottom:14px}
.foot-col li{list-style:none;color:#e3e6ee;font-size:12.5px;line-height:26px}
.foot-col li::before{content:"› ";color:#e3e6ee}
.foot-col.info li::before{content:none}
.foot-col.info li{display:flex;align-items:center;gap:10px;line-height:32px}
.bottom-bar{left:0;top:4938px;width:1200px;height:79px;background:var(--red)}
.bottom-bar p{position:absolute;left:97px;top:31px;color:var(--white);font-size:12.5px}
.socials{position:absolute;right:105px;top:24px;display:flex;gap:10px}
.socials span{width:30px;height:30px;border:1.5px solid var(--white);border-radius:50%}
</style>
</head>
<body>

<!-- HERO -->
<section class="photo hero" role="img" aria-label="Two-storey house with a white picket fence at sunset"></section>
<div class="abs brand"><span class="mark"></span>YARDLINE WORKS</div>
<nav class="abs nav"><a>HOME</a><a>ABOUT US</a><a>SERVICES</a><a>GALLERY</a><a>CONTACT US</a></nav>
<h1 class="abs hero-title">Secure. Stylish.<br>Built to Last.</h1>
<div class="abs strip">
  <div class="item active"><div class="thumb" role="img" aria-label="Worker repairing a fence"></div><span>Restoration<br>and Maintenance</span></div>
  <div class="item"><div class="thumb" role="img" aria-label="Installer at work"></div><span>Fast and<br>Reliable Services</span></div>
  <div class="item"><div class="thumb" role="img" aria-label="Team of fence installers"></div><span>Skilled and<br>Trained Experts</span></div>
  <div class="arrows"><span>←</span><span>→</span></div>
</div>

<!-- ABOUT -->
<div class="abs about-ring"></div>
<div class="photo about-photo" role="img" aria-label="Worker in yellow cap building a brick fence pillar"></div>
<div class="abs about-eyebrow eyebrow">ABOUT</div>
<h2 class="abs h2 about-title">ABOUT YARDLINE WORKS</h2>
<p class="abs about-quote">Lorem Ipsum is simply dummy text of the printing and typesetting industry. Lorem Ipsum has been the industry's standard dummy text ever since the 1500s, when an unknown printer took a galley of type and scrambled it to make a type specimen book. It has survived not</p>
<h3 class="abs mission-title">Our Mission</h3>
<p class="abs mission-text">Lorem Ipsum is simply dummy text of the printing and typesetting industry. Lorem Ipsum has been the industry's standard dummy text ever scrambled it to make a type specimen book. It has survived not only five centuries, but also the leap into electronic typesetting, remaining</p>
<div class="abs btn-dark">Get a Free Estimate</div>
<div class="abs demo">Request a Demo <span class="play"><svg width="12" height="12" viewBox="0 0 12 12"><path d="M2 1l9 5-9 5z" fill="#fff"/></svg></span></div>

<!-- BANNER -->
<section class="photo banner" role="img" aria-label="White lattice garden fence in front of trees with green hedge"></section>
<div class="abs banner-notch"></div>
<h2 class="abs banner-title">TRANSFORM YOUR PROPERTY<br>WITH A STUNNING FENCE</h2>
<p class="abs banner-text">Call us at 555-0142-316 or click the button below to get in touch with us!</p>
<div class="abs btn-white">Get a Free Estimate</div>

<!-- SERVICES -->
<h2 class="abs section-title h2 services-title" style="font-size:38px">OUR SERVICES</h2>
<svg width="0" height="0" style="position:absolute">
  <defs>
    <g id="fence-icon" fill="none" stroke="#fff" stroke-width="2.5">
      <path d="M6 14v26M16 10v30M26 10v30M36 14v26M3 20h36M3 32h36"/>
    </g>
  </defs>
</svg>
<div class="abs card" style="left:97px;top:1831px"><div class="icon"><svg width="42" height="44"><use href="#fence-icon"/></svg></div><h3>Residential Fencing</h3><p>Lorem Ipsum is simply dummy text typesetting industry has industry</p></div>
<div class="abs card" style="left:350px;top:1831px"><div class="icon"><svg width="42" height="44"><use href="#fence-icon"/></svg></div><h3>Commercial Fencing</h3><p>Lorem Ipsum is simply dummy text typesetting industry has industry</p></div>
<div class="abs card" style="left:604px;top:1831px"><div class="icon"><svg width="42" height="44"><use href="#fence-icon"/></svg></div><h3>Wood Fencing</h3><p>Lorem Ipsum is simply dummy text typesetting industry has industry</p></div>
<div class="abs card" style="left:857px;top:1831px"><div class="icon"><svg width="42" height="44"><use href="#fence-icon"/></svg></div><h3>Iron Fencing</h3><p>Lorem Ipsum is simply dummy text typesetting industry has industry</p></div>
<div class="abs card" style="left:97px;top:2088px"><div class="icon"><svg width="42" height="44"><use href="#fence-icon"/></svg></div><h3>Pool Fences</h3><p>Lorem Ipsum is simply dummy text typesetting industry has industry</p></div>
<div class="abs card" style="left:350px;top:2088px"><div class="icon"><svg width="42" height="44"><use href="#fence-icon"/></svg></div><h3>Security Fences</h3><p>Lorem Ipsum is simply dummy text typesetting industry has industry</p></div>
<div class="abs card" style="left:604px;top:2088px"><div class="icon"><svg width="42" height="44"><use href="#fence-icon"/></svg></div><h3>Chain Link Fencing</h3><p>Lorem Ipsum is simply dummy text typesetting industry has industry</p></div>
<div class="abs card" style="left:857px;top:2088px"><div class="icon"><svg width="42" height="44"><use href="#fence-icon"/></svg></div><h3>Vinyl Fence</h3><p>Lorem Ipsum is simply dummy text typesetting industry has industry</p></div>

<!-- CTA -->
<section class="abs cta">
  <h2>HAVE A PROJECT IN MIND?</h2>
  <p>Please contact Yardline Works. We are ready to help.</p>
  <div class="btn-red"><svg width="18" height="14" viewBox="0 0 18 14"><rect x="1" y="1" width="16" height="12" fill="none" stroke="#fff" stroke-width="1.5"/><path d="M1 1l8 7 8-7" fill="none" stroke="#fff" stroke-width="1.5"/></svg>CONTACT US</div>
</section>

<!-- RECENT WORK -->
<p class="abs section-title work-eyebrow">LATEST PROJECTS</p>
<h2 class="abs section-title h2 work-title">OUR RECENT WORK</h2>
<div class="photo" style="left:0;top:2941px;width:316px;height:361px;background:linear-gradient(180deg,#9fb8c6 0%,#c9d5d9 50%,#8a8a5a 70%,#7b7b7b 100%)" role="img" aria-label="Security fence with barbed wire along a road"></div>
<div class="photo" style="left:327px;top:2922px;width:546px;height:399px;background:linear-gradient(180deg,#3f7fd1 0%,#8fb5e0 30%,#a8692e 55%,#6a8a3a 80%,#9a9a9a 100%)" role="img" aria-label="House with a tall wooden privacy fence and garden"></div>
<div class="abs work-label">RESIDENTIAL PROJECTS</div>
<div class="photo" style="left:886px;top:2941px;width:314px;height:361px;background:linear-gradient(180deg,#a9c7e6 0%,#e8eef4 40%,#f5f5f5 55%,#8bab3c 75%,#c8b83a 100%)" role="img" aria-label="White vinyl rail fence in a flower meadow"></div>
<div class="abs dots"><span></span><span></span><span></span><span></span><span></span></div>

<!-- FEEDBACK -->
<h2 class="abs section-title feedback-title">Feedback from<br>Satisfied Customers</h2>
<div class="abs review" style="left:97px;top:3510px"><div class="stars"><span></span><span></span><span></span><span></span><span></span></div><p>Lorem Ipsum is simply dummy text of the printing and typesetting industry. Lorem Ipsum has been the industry's standard dummy text ever since the 1500s, when an unknown printer took a galley of type and scrambled it to make a type specimen book</p></div>
<div class="abs review" style="left:612px;top:3510px"><div class="stars"><span></span><span></span><span></span><span></span><span></span></div><p>Lorem Ipsum is simply dummy text of the printing and typesetting industry. Lorem Ipsum has been the industry's standard dummy text ever since the 1500s, when an unknown printer took a galley of type and scrambled it to make a type specimen book</p></div>
<div class="abs person" style="left:152px;top:3733px"><div class="avatar" role="img" aria-label="Portrait of customer"></div><div><b>Dana Whitlock</b><small>Managing Director</small></div></div>
<div class="abs person" style="left:665px;top:3733px"><div class="avatar" role="img" aria-label="Portrait of customer"></div><div><b>Omar Reyes</b><small>Co Funder</small></div></div>

<!-- CONTACT -->
<div class="abs contact-bg"></div>
<h2 class="abs h2 contact-title">GET IN TOUCH</h2>
<div class="abs field" style="left:97px;top:4017px;width:243px;height:48px">Enter your name</div>
<div class="abs field" style="left:349px;top:4017px;width:243px;height:48px">Enter your last name</div>
<div class="abs field" style="left:97px;top:4084px;width:243px;height:48px">Enter your email</div>
<div class="abs field" style="left:349px;top:4084px;width:243px;height:48px">Enter your phone</div>
<div class="abs field" style="left:97px;top:4151px;width:495px;height:102px">Enter your comments</div>
<div class="abs btn-red btn-submit">SUBMIT NOW</div>
<div class="photo contact-photo" role="img" aria-label="White picket fence with yellow lilies against blue sky"></div>

<!-- FOOTER -->
<footer class="abs footer"></footer>
<h2 class="abs section-title signup-title">SIGN UP FOR EXCLUSIVE UPDATES!</h2>
<div class="abs signup-input"><svg width="22" height="16" viewBox="0 0 22 16"><rect x="1" y="1" width="20" height="14" fill="none" stroke="#c9ceda" stroke-width="1.3"/><path d="M1 1l10 8 10-8" fill="none" stroke="#c9ceda" stroke-width="1.3"/></svg>Enter your email</div>
<div class="abs btn-red btn-sub">SUBSCRIBE NOW</div>
<div class="abs foot-brand"><span class="mark"></span>YARDLINE WORKS</div>
<div class="abs foot-col" style="left:430px;top:4718px"><h4>QUICK LINKS</h4><ul><li>Home</li><li>About Us</li><li>Services</li><li>Gallery</li><li>Contact Us</li></ul></div>
<div class="abs foot-col" style="left:646px;top:4716px"><h4>OUR SERVICES</h4><ul><li>Residential Fencing</li><li>Commercial Fencing</li><li>Wood Fencing</li><li>Chain Link Fencing</li><li>Iron Fencing</li></ul></div>
<div class="abs foot-col info" style="left:881px;top:4716px"><h4>CONTACT INFO</h4><ul>
  <li><svg width="12" height="14" viewBox="0 0 12 14"><path d="M6 13S1 8 1 5a5 5 0 0110 0c0 3-5 8-5 8z" fill="none" stroke="#e3e6ee"/><circle cx="6" cy="5" r="1.6" fill="#e3e6ee"/></svg>Lorem Ipsum simply dummy text</li>
  <li><svg width="14" height="10" viewBox="0 0 14 10"><rect x=".5" y=".5" width="13" height="9" fill="none" stroke="#e3e6ee"/><path d="M.5.5l6.5 5 6.5-5" fill="none" stroke="#e3e6ee"/></svg>info@yardlineworks.example</li>
  <li><svg width="13" height="13" viewBox="0 0 13 13"><path d="M3 1l2 3-1.5 1.5a7 7 0 004 4L9 8l3 2-1.5 2C6 12 1 7 1 2.5z" fill="none" stroke="#e3e6ee"/></svg>0400 555 923</li>
  <li><svg width="13" height="13" viewBox="0 0 13 13"><circle cx="6.5" cy="6.5" r="5.8" fill="none" stroke="#e3e6ee"/><path d="M.7 6.5h11.6M6.5.7c-3 3.5-3 8 0 11.6M6.5.7c3 3.5 3 8 0 11.6" fill="none" stroke="#e3e6ee"/></svg>www.yardlineworks.example</li>
</ul></div>
<div class="abs bottom-bar"><p>© 2025 yardlineworks.example. All Rights Reserved</p><div class="socials"><span></span><span></span><span></span><span></span></div></div>

</body>
</html>
```